New automotive search style homepage

Looking for someone that can create a new homepage layout for my company. What we currently have is a little plain above the fold. We are an automotive technology company, where we take over the negotiation for customers, and perhaps we can have a design that appeals to that idea more. The current chat container is our only way to search currently, but would love to have a hybrid chat and manual search container, with the manual fields being make and model. This shouldn't have a toggle, but a seamless split view housing both features. You can see current design of our site at motorlane.net

Target Market(s)

Car buyers

Industry/Entity Type

Automotive

Number of Pages Required

1 page

Colors
0054AA
0677BA
7BADD7
CADEEF
E8F1F8

Requirements
Must have
• Above the fold is the most important

```html
<!DOCTYPE html>
<html lang="en">
<head>
<meta charset="utf-8">
<title>MotorLane – Car buying, reversed</title>
<link href="https://fonts.googleapis.com/css2?family=Inter:wght@400;500;600;700;800&display=swap" rel="stylesheet">
<style>
:root{
  --blue:#1381f5;
  --blue-deep:#0054AA;
  --blue-mid:#0677BA;
  --blue-soft:#7BADD7;
  --blue-pale:#CADEEF;
  --blue-mist:#E8F1F8;
  --accent:#4f8ef7;
  --ink:#111418;
  --ink-2:#2b2f36;
  --grey:#6b7280;
  --grey-2:#9aa1ab;
  --line:#e3e6ea;
  --panel:#f5f7fa;
  --footer:#121316;
  --green:#18a058;
}
*{box-sizing:border-box;margin:0;padding:0}
html,body{width:1200px;height:2769px;overflow:hidden}
body{font-family:'Inter',sans-serif;color:var(--ink);background:#fff}
a{color:inherit;text-decoration:none}

/* HERO */
.hero{position:relative;height:600px;color:#fff;overflow:hidden}
.hero-bg{position:absolute;inset:0;background:radial-gradient(ellipse at 35% 35%,#4a4d52 0%,#2a2c30 35%,#141518 70%,#0b0b0d 100%)}
.hero-bg::after{content:"";position:absolute;inset:0;background:linear-gradient(180deg,rgba(0,0,0,.35),rgba(0,0,0,.15) 40%,rgba(0,0,0,.45))}
.nav{position:absolute;top:0;left:0;right:0;height:66px;display:flex;align-items:center;padding:0 24px 0 22px;z-index:2}
.logo{font-weight:800;font-size:19px;letter-spacing:-.3px;color:var(--blue)}
.nav-links{display:flex;gap:28px;margin-left:44px;font-size:10.5px;font-weight:600}
.nav-links .pro{color:var(--accent);display:flex;align-items:center;gap:5px}
.nav-right{margin-left:auto;display:flex;align-items:center;gap:40px;font-size:10.5px;font-weight:600}
.burger{width:28px;display:flex;flex-direction:column;gap:4px;align-items:flex-end}
.burger span{height:1.5px;background:var(--blue);display:block}
.hero-inner{position:absolute;left:245px;width:708px;top:170px;z-index:2}
.hero h1{text-align:center;font-size:39px;font-weight:700;letter-spacing:-.6px}
.hero h1 em{font-style:normal;color:var(--accent)}
.hero .lead{text-align:center;font-size:15px;margin-top:13px}
.search-row{display:flex;gap:14px;margin-top:30px;align-items:flex-end}
.field{width:131px}
.field label{display:block;font-size:11px;font-weight:700;margin-bottom:8px}
.control{height:35px;background:#fff;border-radius:4px;color:#222;font-size:11.5px;display:flex;align-items:center;justify-content:space-between;padding:0 11px}
.control .caret{width:0;height:0;border-left:4px solid transparent;border-right:4px solid transparent;border-top:5px solid #222}
.btn-search{width:130px;height:35px;background:var(--blue);color:#fff;font-size:11.5px;font-weight:600;border-radius:4px;display:flex;align-items:center;justify-content:center}
.chat-label{font-size:11px;font-weight:700;margin-top:39px;margin-bottom:10px}
.chat{position:relative;height:79px;background:#fff;border-radius:5px;color:#444;font-size:11px;padding:13px 14px}
.chat .send{position:absolute;right:10px;bottom:10px;width:22px;height:22px;border-radius:50%;background:var(--blue);display:flex;align-items:center;justify-content:center}

/* HOW */
.how{height:403px;background:linear-gradient(180deg,#0e2a88 0%,#1a45c4 55%,#2157d8 100%);color:#fff;position:relative}
.how h2{text-align:center;font-size:24px;font-weight:700;padding-top:49px}
.steps{display:flex;position:absolute;left:173px;top:134px}
.step{width:216px}
.step svg{display:block;margin-bottom:24px}
.step h3{font-size:16.5px;font-weight:600;margin-bottom:12px}
.step p{font-size:11.5px;line-height:18px;color:#e2e9ff;width:180px}
.btn-watch{position:absolute;left:508px;top:311px;width:180px;height:39px;background:var(--blue);border-radius:4px;font-size:12px;font-weight:600;display:flex;align-items:center;justify-content:center}

/* DEALS */
.deals{height:572px;position:relative;overflow:hidden}
.deals h2{position:absolute;left:173px;top:50px;font-size:24px;font-weight:600}
.btn-outline{position:absolute;border:1px solid var(--blue);color:var(--blue);border-radius:4px;font-size:10px;font-weight:600;display:flex;align-items:center;justify-content:center;background:#fff}
.deals .btn-outline{left:906px;top:48px;width:120px;height:29px}
.cards{position:absolute;top:112px;left:-43px;display:flex;gap:12px}
.card{width:204px;height:405px;border:1px solid var(--line);border-radius:4px;background:#fff;position:relative;overflow:hidden}
.card .photo{height:155px;position:relative}
.card .heart{position:absolute;right:9px;top:9px;width:18px;height:18px;border-radius:50%;background:rgba(255,255,255,.85);display:flex;align-items:center;justify-content:center}
.card .body{padding:12px 11px 0}
.card h4{font-size:12.5px;font-weight:600;line-height:18px}
.card .trim{font-size:9px;color:var(--grey);margin-top:2px}
.card .price-row{display:flex;justify-content:space-between;align-items:center;margin-top:12px}
.card .price{font-size:16.5px;font-weight:500}
.card .miles{font-size:9px;color:var(--ink-2);display:flex;align-items:center;gap:3px}
.card .msrp{font-size:9px;color:var(--grey);margin-top:3px}
.card .msrp s{color:var(--grey)}
.card .msrp b{color:var(--green);font-weight:600;margin-left:4px}
.card .mo{font-size:9px;color:var(--blue);margin-top:3px}
.card .days{display:inline-block;font-size:8.5px;color:var(--grey);background:#f2f3f5;padding:3px 6px;margin-top:10px;border-radius:2px}
.card .colors{margin-top:12px;font-size:9px;line-height:15px;color:var(--ink-2)}
.card .colors span{display:flex;align-items:center;gap:5px}
.card .colors i{width:7px;height:7px;border-radius:50%;display:inline-block}
.card .loc{position:absolute;left:11px;right:11px;bottom:14px;border-top:1px solid var(--line);padding-top:16px;font-size:9px;color:var(--ink-2);display:flex;align-items:center;gap:5px}

/* COMPARE */
.compare{height:412px;background:var(--panel);position:relative}
.compare .intro{position:absolute;left:173px;top:70px;width:260px}
.compare h2{font-size:25px;font-weight:600;line-height:29px;letter-spacing:-.3px}
.compare .intro p{font-size:11px;color:var(--grey);line-height:20px;margin-top:20px}
.stats{margin-top:19px;display:flex;flex-direction:column;gap:16px}
.stats div{display:flex;align-items:center;gap:10px;font-size:11px;font-weight:600;color:var(--blue)}
.table{position:absolute;left:473px;top:55px;width:553px;display:flex;border-radius:4px;overflow:hidden;box-shadow:0 1px 3px rgba(0,0,0,.08)}
.col{width:50%}
.col.old{background:#fff;border:1px solid var(--line);border-right:none}
.col.new{background:var(--blue);color:#fff}
.col .head{height:60px;display:flex;align-items:center;justify-content:center;font-size:17px;font-weight:500;border-bottom:1px solid var(--line)}
.col.old .head{color:#4a4f57}
.col.new .head{font-weight:800;font-size:19px;border-bottom-color:rgba(255,255,255,.3)}
.col .row{height:40px;display:flex;align-items:center;padding-left:22px;font-size:11px;font-weight:600;border-bottom:1px solid var(--line)}
.col.old .row{color:#50555d}
.col.new .row{border-bottom-color:rgba(255,255,255,.3)}
.col .row:last-child{border-bottom:none;height:46px}

/* FAQ */
.faq{height:432px;position:relative}
.faq h2{text-align:center;font-size:24px;font-weight:600;padding-top:50px}
.faq-list{position:absolute;left:316px;top:113px;width:566px}
.faq-item{border-bottom:1px solid var(--line);padding:0 0 18px;margin-bottom:18px}
.faq-item .q{display:flex;justify-content:space-between;align-items:center;font-size:16px;font-weight:600}
.faq-item.open .q{color:var(--blue)}
.faq-item .a{font-size:11px;color:var(--grey);line-height:17px;margin-top:14px;width:530px}
.toggle{width:16px;height:16px;border-radius:50%;display:flex;align-items:center;justify-content:center;background:#e9ebee}
.faq-item.open .toggle{background:var(--blue)}
.faq .btn-outline{left:549px;top:352px;width:100px;height:30px}

/* FOOTER */
.footer{height:350px;background:var(--footer);color:#fff;position:relative}
.footer .brand{position:absolute;left:173px;top:44px}
.footer .brand .logo{font-size:19px}
.footer .tag{font-size:12px;font-weight:600;margin-top:14px}
.contact{margin-top:20px;display:flex;flex-direction:column;gap:10px;font-size:11.5px}
.contact div{display:flex;align-items:center;gap:10px}
.contact .ic{width:19px;height:19px;border-radius:50%;background:#2a2c31;display:flex;align-items:center;justify-content:center}
.fcols{position:absolute;left:461px;top:52px;display:flex}
.fcol{width:144px}
.fcol h5{font-size:12.5px;font-weight:500;color:#a8adb5;margin-bottom:18px}
.fcol a{display:block;font-size:11.5px;margin-bottom:11px}
.fbar{position:absolute;left:173px;right:173px;top:230px;height:40px;display:flex;align-items:center;justify-content:space-between;border-bottom:1px solid #2a2c31}
.badges{display:flex;gap:22px;font-size:9.5px;color:#9aa0a8}
.badges span{display:flex;align-items:center;gap:5px}
.social{display:flex;gap:17px}
.social i{width:12px;height:12px;border-radius:50%;border:1.5px solid #fff;display:block}
.legal{position:absolute;left:173px;right:173px;top:292px;font-size:9px;color:#9aa0a8}
.legal p+p{font-size:6.8px;line-height:10.5px;margin-top:9px}
</style>
</head>
<body>

<header class="hero">
  <div class="hero-bg" role="img" aria-label="Dark close-up photo of a car's headlight and front grille"></div>
  <nav class="nav">
    <a class="logo" href="#">MotorLane</a>
    <div class="nav-links">
      <a href="#">Search</a><a href="#">Sell Your Car</a><a href="#">Deals</a><a href="#">Insurance</a><a href="#">Research</a>
      <a class="pro" href="#"><svg width="11" height="9" viewBox="0 0 11 9"><path d="M1 2l2.5 2.5L5.5 1l2 3.5L10 2l-1 6H2z" fill="none" stroke="#4f8ef7" stroke-width="1.2" stroke-linejoin="round"/></svg>PRO</a>
    </div>
    <div class="nav-right">
      <a href="#">Login</a>
      <div class="burger"><span style="width:28px"></span><span style="width:22px"></span><span style="width:28px"></span></div>
    </div>
  </nav>
  <div class="hero-inner">
    <h1>Car buying, <em>reversed</em></h1>
    <p class="lead">Find your next car. MotorLane Experts negotiate the best price.</p>
    <div class="search-row">
      <div class="field"><label>Make</label><div class="control">Select make<span class="caret"></span></div></div>
      <div class="field"><label>Model</label><div class="control">Select model<span class="caret"></span></div></div>
      <div class="field"><label>Price Range</label><div class="control">$1,000-$10,000<span class="caret"></span></div></div>
      <div class="field"><label>ZIP Code</label><div class="control">12345</div></div>
      <a class="btn-search" href="#">Search Your Car</a>
    </div>
    <p class="chat-label">Or find your spesific car</p>
    <div class="chat">I want a hybrid with AWD and heated seats under $40k...
      <span class="send"><svg width="10" height="10" viewBox="0 0 10 10"><path d="M5 9V1M1.5 4.5L5 1l3.5 3.5" stroke="#fff" stroke-width="1.5" fill="none" stroke-linecap="round"/></svg></span>
    </div>
  </div>
</header>

<section class="how">
  <h2>How MotorLane works</h2>
  <div class="steps">
    <div class="step">
      <svg width="44" height="44" viewBox="0 0 44 44" fill="none" stroke="#7BADD7" stroke-width="2" stroke-linecap="round" stroke-linejoin="round"><path d="M6 26v-7l4-8h18l4 8v7z"/><path d="M6 26v5h5v-5M27 26v3"/><circle cx="12" cy="21" r="1.5"/><path d="M17 21h6"/><circle cx="33" cy="33" r="5"/><path d="M37 37l4 4"/></svg>
      <h3>1. Find Your Car</h3>
      <p>Search our inventory for the make, model, and year you want.</p>
    </div>
    <div class="step">
      <svg width="44" height="44" viewBox="0 0 44 44" fill="none" stroke="#7BADD7" stroke-width="2" stroke-linecap="round" stroke-linejoin="round"><path d="M18 6h18a5 5 0 015 5v8a5 5 0 01-5 5h-2v5l-5-5"/><path d="M8 16h18a5 5 0 015 5v8a5 5 0 01-5 5H14l-6 5v-5a5 5 0 01-5-5v-8a5 5 0 015-5z"/><path d="M10 23h14M10 28h10"/></svg>
      <h3>2. Start AI Negotiation</h3>
      <p>MotorLane makes dealers compete for you.</p>
    </div>
    <div class="step">
      <svg width="44" height="44" viewBox="0 0 44 44" fill="none" stroke="#7BADD7" stroke-width="2" stroke-linecap="round" stroke-linejoin="round"><path d="M26 10H6v20h6v7l7-7h15V20"/><path d="M11 17h12M11 23h16"/><path d="M34 3l2 4 4 .5-3 3 1 4-4-2-4 2 1-4-3-3 4-.5z"/></svg>
      <h3>3. Review Your Offers</h3>
      <p>Watch competing offers come in from multiple dealers.</p>
    </div>
    <div class="step">
      <svg width="44" height="44" viewBox="0 0 44 44" fill="none" stroke="#7BADD7" stroke-width="2" stroke-linecap="round" stroke-linejoin="round"><path d="M22 38L7 23a9 9 0 0115-10 9 9 0 0115 10z"/><path d="M15 20l6-4 9 9M18 27l4 4M21 24l4 4M15 30l3 3"/></svg>
      <h3>4. Choose Your Deal</h3>
      <p>Pick the winning offer and drive it home.</p>
    </div>
  </div>
  <a class="btn-watch" href="#">Watch Dealer Compete</a>
</section>

<section class="deals">
  <h2>Latest daily deals</h2>
  <a class="btn-outline" href="#">View All Daily Deals</a>
  <div class="cards">
    <article class="card">
      <div class="photo" role="img" aria-label="Photo of a maroon hatchback on a dealer lot" style="background:linear-gradient(180deg,#25304a 0 12%,#c9ccd1 12%,#8a8f96 60%,#5a2a32 100%)"><span class="heart"><svg width="9" height="8" viewBox="0 0 9 8"><path d="M4.5 7.5L1 4a2 2 0 013.5-2.5A2 2 0 018 4z" fill="none" stroke="#555" stroke-width="1"/></svg></span></div>
      <div class="body">
        <h4>2016 Corso Clubline</h4>
        <div class="price-row" style="margin-top:22px"><span class="price">$12,348</span><span class="miles">◠ 81.043 mi</span></div>
        <div class="mo">Est. $189/mo*</div>
        <span class="days">86 days on market</span>
      </div>
      <div class="loc">📍 Minneapolis, MN</div>
    </article>
    <article class="card">
      <div class="photo" role="img" aria-label="Photo of a black SUV in a checkered showroom" style="background:linear-gradient(180deg,#b3261e 0 6%,#bfc2c6 6%,#6f7378 55%,#2c2e31 100%)"><span class="heart"><svg width="9" height="8" viewBox="0 0 9 8"><path d="M4.5 7.5L1 4a2 2 0 013.5-2.5A2 2 0 018 4z" fill="none" stroke="#555" stroke-width="1"/></svg></span></div>
      <div class="body">
        <h4>New 2026 Ridgeback Grand Tourer</h4>
        <div class="trim">Trailside</div>
        <div class="price-row"><span class="price">$39.186</span><span class="miles">◠ 1.255 mi</span></div>
        <div class="msrp">MSRP: <s>$49.020</s><b>20.1% off</b></div>
        <div class="mo">Est. $571/mo*</div>
        <span class="days">124 days on market</span>
        <div class="colors"><span><i style="background:#111"></i>Black</span><span><i style="background:#111"></i>Black</span></div>
      </div>
      <div class="loc">📍 Elk River, MN</div>
    </article>
    <article class="card">
      <div class="photo" role="img" aria-label="Photo of a black three-row SUV outside a dealership" style="background:linear-gradient(180deg,#e9eaec 0 10%,#9ea3a9 10%,#5d6268 50%,#23252a 100%)"><span class="heart"><svg width="9" height="8" viewBox="0 0 9 8"><path d="M4.5 7.5L1 4a2 2 0 013.5-2.5A2 2 0 018 4z" fill="none" stroke="#555" stroke-width="1"/></svg></span></div>
      <div class="body">
        <h4>Certified 2023 Kestra Tellus</h4>
        <div class="price-row" style="margin-top:22px"><span class="price">$29.988</span><span class="miles">◠ 77.484 mi</span></div>
        <div class="mo">Est. $439/mo*</div>
        <span class="days">29 days on market</span>
        <div class="colors"><span><i style="background:#111"></i>Black</span><span><i style="background:#111"></i>Black</span></div>
      </div>
      <div class="loc">📍 White Bear Lake, MN</div>
    </article>
    <article class="card">
      <div class="photo" role="img" aria-label="Photo of a grey electric crossover in snow" style="background:linear-gradient(180deg,#3a5fa8 0 25%,#b8c0cb 25%,#dfe3e8 70%,#9aa1a9 100%)"><span class="heart"><svg width="9" height="8" viewBox="0 0 9 8"><path d="M4.5 7.5L1 4a2 2 0 013.5-2.5A2 2 0 018 4z" fill="none" stroke="#555" stroke-width="1"/></svg></span></div>
      <div class="body">
        <h4>New 2026 Calder Solstice EV</h4>
        <div class="trim">Lt</div>
        <div class="price-row"><span class="price">$27.350</span><span class="miles">◠ 2.511 mi</span></div>
        <div class="msrp">MSRP: <s>$36.890</s><b>25.9% off</b></div>
        <div class="mo">Est. $401/mo*</div>
        <span class="days">45 days on market</span>
        <div class="colors"><span><i style="background:#7a7d82"></i>Gray</span><span><i style="background:#111"></i>Black</span></div>
      </div>
      <div class="loc">📍 Fridley, MN</div>
    </article>
    <article class="card">
      <div class="photo" role="img" aria-label="Photo of a white coupe SUV in a studio" style="background:linear-gradient(180deg,#e4e5e7 0%,#cfd1d4 55%,#a9acb0 100%)"><span class="heart"><svg width="9" height="8" viewBox="0 0 9 8"><path d="M4.5 7.5L1 4a2 2 0 013.5-2.5A2 2 0 018 4z" fill="none" stroke="#555" stroke-width="1"/></svg></span></div>
      <div class="body">
        <h4>Certified 2025 Lumeon QS55</h4>
        <div class="trim">Luxe</div>
        <div class="price-row"><span class="price">$37.968</span><span class="miles">◠ 7.235 mi</span></div>
        <div class="mo">Est. $554/mo*</div>
        <span class="days">51 days on market</span>
        <div class="colors"><span><i style="background:#fff;border:1px solid #ccc"></i>White</span><span><i style="background:#7a7d82"></i>Gray</span></div>
      </div>
      <div class="loc">📍 Minneapolis, MN</div>
    </article>
    <article class="card">
      <div class="photo" role="img" aria-label="Photo of a black full-size SUV outside a dealership" style="background:linear-gradient(180deg,#9fb2c8 0 30%,#6d665e 30%,#2b2c2f 85%,#000 85%)"><span class="heart"><svg width="9" height="8" viewBox="0 0 9 8"><path d="M4.5 7.5L1 4a2 2 0 013.5-2.5A2 2 0 018 4z" fill="none" stroke="#555" stroke-width="1"/></svg></span></div>
      <div class="body">
        <h4>Used 2015 Norvik Fleetline</h4>
        <div class="price-row" style="margin-top:22px"><span class="price">$13.472</span><span class="miles">◠ 109.880 mi</span></div>
        <div class="mo">Est. $201/mo*</div>
        <span class="days">629 days on market</span>
        <div class="colors"><span><i style="background:#111"></i>Black</span><span><i style="background:#111"></i>Black</span></div>
      </div>
      <div class="loc">📍 Minneapolis, MN</div>
    </article>
  </div>
</section>

<section class="compare">
  <div class="intro">
    <h2>The Old Way vs<br>The MotorLane Way</h2>
    <p>Our platform solves both problems by providing a place where Buyers can easily enter what they're looking for and Dealers can easily quote someone ready and able to buy.</p>
    <div class="stats">
      <div><svg width="13" height="11" viewBox="0 0 13 11" fill="none" stroke="#1381f5" stroke-width="1.2"><circle cx="5" cy="3" r="2.2"/><path d="M1 10c0-2.5 2-4 4-4s4 1.5 4 4M9 1a2 2 0 010 4M10.5 6.5c1 .6 1.8 1.8 1.8 3.5"/></svg>10,000+ Active Buyers</div>
      <div><svg width="13" height="13" viewBox="0 0 13 13" fill="none" stroke="#1381f5" stroke-width="1.2"><path d="M6.5 1L11 3v3.5c0 3-2.2 4.8-4.5 5.5C4.2 11.3 2 9.5 2 6.5V3z"/></svg>Verified Dealers</div>
      <div><svg width="13" height="13" viewBox="0 0 13 13" fill="none" stroke="#1381f5" stroke-width="1.2"><circle cx="6.5" cy="6.5" r="5.5"/><circle cx="6.5" cy="6.5" r="3"/><circle cx="6.5" cy="6.5" r=".8" fill="#1381f5"/></svg>95% Match Accuracy</div>
    </div>
  </div>
  <div class="table">
    <div class="col old">
      <div class="head">The Old Way</div>
      <div class="row">You visit dealership after dealership</div>
      <div class="row">Every salesperson has an agenda</div>
      <div class="row">Inconsistent pricing and hidden fees</div>
      <div class="row">Hours of back-and-forth negotiation</div>
      <div class="row">You leave wondering if you got played</div>
      <div class="row">Pressure to decide on dealer's timeline</div>
    </div>
    <div class="col new">
      <div class="head">MotorLane</div>
      <div class="row">Dealers come to you</div>
      <div class="row">MotorLane works for buyers, not dealers</div>
      <div class="row">Transparent pricing from competing dealers</div>
      <div class="row">Built-in negotiation handles it</div>
      <div class="row">You leave knowing you got the best deal</div>
      <div class="row">Your timeline. Your decision</div>
    </div>
  </div>
</section>

<section class="faq">
  <h2>Frequently Asked Questions</h2>
  <div class="faq-list">
    <div class="faq-item open">
      <div class="q">Does MotorLane cost anything to use?<span class="toggle"><svg width="8" height="8" viewBox="0 0 8 8"><path d="M4 1v6M1 4h6" stroke="#fff" stroke-width="1.4"/></svg></span></div>
      <p class="a">MotorLane marketplace is completely free for browsers. If you're looking to buy and want to utilize our negotiation technology, we have multiple upgrade packages available.</p>
    </div>
    <div class="faq-item">
      <div class="q">Do I still have to negotiate with dealerships?<span class="toggle"><svg width="8" height="8" viewBox="0 0 8 8"><path d="M1.5 4h5" stroke="#555" stroke-width="1.2"/></svg></span></div>
    </div>
    <div class="faq-item">
      <div class="q">How do I know the price is fair?<span class="toggle"><svg width="8" height="8" viewBox="0 0 8 8"><path d="M1.5 4h5" stroke="#555" stroke-width="1.2"/></svg></span></div>
    </div>
  </div>
  <a class="btn-outline" href="#">View All FAQs</a>
</section>

<footer class="footer">
  <div class="brand">
    <div class="logo">MotorLane</div>
    <p class="tag">The smarter way to buy your next car</p>
    <div class="contact">
      <div><span class="ic"><svg width="9" height="7" viewBox="0 0 9 7"><rect x=".5" y=".5" width="8" height="6" rx="1" fill="#fff"/><path d="M.8 1l3.7 2.6L8.2 1" stroke="#2a2c31" fill="none" stroke-width=".8"/></svg></span>hello@motorlane.net</div>
      <div><span class="ic"><svg width="8" height="10" viewBox="0 0 8 10"><path d="M4 9.5S.5 6 .5 3.8a3.5 3.5 0 017 0C7.5 6 4 9.5 4 9.5z" fill="#fff"/><circle cx="4" cy="3.8" r="1.2" fill="#2a2c31"/></svg></span>Chicago, IL</div>
    </div>
  </div>
  <div class="fcols">
    <div class="fcol"><h5>Company</h5><a href="#">About Us</a><a href="#">Contact</a><a href="#">Affiliate Program</a></div>
    <div class="fcol"><h5>For Buyers</h5><a href="#">Search</a><a href="#">Daily Deals</a><a href="#">How It Works</a><a href="#">Car Value Calculator</a></div>
    <div class="fcol"><h5>Resources</h5><a href="#">Guides</a><a href="#">Research</a><a href="#">FAQ</a></div>
    <div class="fcol"><h5>Legal</h5><a href="#">Report Problem</a><a href="#">Terms &amp; Conditions</a><a href="#">Privacy Policy</a></div>
  </div>
  <div class="fbar">
    <div class="badges">
      <span><svg width="10" height="11" viewBox="0 0 10 11" fill="none" stroke="#9aa0a8"><path d="M5 .8L9 2.5v3c0 2.4-1.8 3.8-4 4.6C2.8 9.3 1 7.9 1 5.5v-3z"/></svg>SSL Secured</span>
      <span><svg width="9" height="11" viewBox="0 0 9 11" fill="none" stroke="#9aa0a8"><circle cx="4.5" cy="4" r="3"/><path d="M2.5 6.5L2 10.5l2.5-1.3 2.5 1.3-.5-4"/></svg>Top Rated</span>
      <span><svg width="11" height="11" viewBox="0 0 11 11" fill="none" stroke="#9aa0a8"><circle cx="5.5" cy="5.5" r="4.8"/><path d="M3.3 5.6l1.5 1.5 3-3"/></svg>Verified Dealers</span>
    </div>
    <div class="social"><i></i><i></i><i></i><i></i><i></i><i></i></div>
  </div>
  <div class="legal">
    <p>© Copyright 2026 MotorLane. All rights reserved.</p>
    <p>MotorLane operates independently and is not sponsored, endorsed, affiliated with, or authorized by any automaker or trademark owner. All listing information, including vehicle details, photos, and pricing, is provided by sellers and third-party data providers. Brand names and vehicle imagery are used solely for identification and descriptive purposes. MotorLane makes no representations or warranties, express or implied, as to the accuracy, completeness, or validity of any such information. All prices and market figures are in U.S. Dollars. Buyers must independently confirm availability, pricing, vehicle condition, and all transaction terms directly with the seller.</p>
  </div>
</footer>

</body>
</html>
```